Bluebrook Irrigation Business Card and Stationary
Business Cards, Envelopes, Stationary, etc.
Simple
Doug Harlan
General Operations Manager
742 Orchard Lane
Irving, TX 75119
doug@irrigatepros.com
www.irrigatepros.com
Li 48391
I want the inside part to list services that we perform.
1. Lawn Sprinkler Repair
2. Lawn Sprinkler Installation
3. Sprinkler System Efficiency Evaluation
4. French/Area Drains
5. Outdoor Lighting
6. Tree/Shrub Planting
7. Landscaping
8. Water Features
9. Sod
10. Backflow Testing
11. Outdoor/Landscape Lighting
12. Soil Test/Analysis
Arrange all of the information as you feel it fits best. I am also getting a PO box today, so the address will e different. I will update that when I have the info. Also, I would like a sticker that we can put on the customers controllers, about business card size that says "call for service," and then has our phone #. I am not opposed to having perfectly rectangular business cards, but am also not sold on it, maybe something with rounded corners.

```html
<!DOCTYPE html>
<html lang="en">
<head>
<meta charset="utf-8">
<title>Bluebrook Irrigation – Business Card Layout</title>
<link href="https://fonts.googleapis.com/css2?family=Open+Sans:ital,wght@0,300;0,400;0,600;0,700;1,400&display=swap" rel="stylesheet">
<style>
  :root{
    --page:#e6e6e6;
    --sheet:#ffffff;
    --label:#8a8a8a;
    --blue-dark:#1363b3;
    --blue-light:#2aa6e2;
    --green-light:#8cc63f;
    --green-dark:#2f9a3e;
    --brand-blue:#1a7cc4;
    --ink:#1e2a1e;
    --ink-soft:#6b6b6b;
    --white:#ffffff;
  }
  *{margin:0;padding:0;box-sizing:border-box}
  html,body{width:1200px;height:838px;overflow:hidden;background:var(--page)}
  body{font-family:"Open Sans",Arial,sans-serif;position:relative}
  .sheet{position:absolute;left:30px;top:14px;width:1140px;height:810px;background:var(--sheet);border:1px solid #d2d2d2}
  .label{position:absolute;width:516px;text-align:center;font-size:22px;color:var(--label);font-weight:400}
  .card{position:absolute;width:516px;height:288px;border-radius:24px;overflow:hidden}
  .card svg.bg{position:absolute;inset:0;width:100%;height:100%}
  .card .t{position:absolute;white-space:nowrap}

  .brand{font-weight:700;color:var(--white)}
  .brand.on-white{color:var(--brand-blue)}
  .brand.small{width:64px;text-align:center;font-size:11px;line-height:1.2}
  .web{color:var(--white);font-weight:600}

  .person-name{font-weight:300;font-size:26px;color:var(--ink-soft);line-height:1}
  .person-title{font-weight:700;font-size:11.5px;color:var(--ink)}
  .contact{font-size:11px;color:var(--ink);line-height:1.35}
  .contact-row{display:flex;align-items:flex-start;gap:7px;margin-bottom:3px}
  .contact-row svg{flex:none;width:12px;height:12px;margin-top:1px}

  .services-title{font-style:italic;font-size:16px;color:var(--ink)}
  .services{list-style:none;font-size:11px;color:var(--ink);line-height:18.2px}
</style>
</head>
<body>
<div class="sheet"></div>

<div class="label" style="left:67px;top:50px">Outside Back</div>
<div class="label" style="left:607px;top:50px">Outside Front</div>
<div class="label" style="left:67px;top:770px">inside</div>
<div class="label" style="left:607px;top:770px">inside</div>

<svg width="0" height="0" style="position:absolute">
  <defs>
    <linearGradient id="blueGrad" x1="0" y1="0" x2="1" y2="0.3">
      <stop offset="0" stop-color="#1b73c4"/>
      <stop offset="1" stop-color="#2aa6e2"/>
    </linearGradient>
    <linearGradient id="greenGrad" x1="0" y1="1" x2="1" y2="0">
      <stop offset="0" stop-color="#a6cf3a"/>
      <stop offset="0.55" stop-color="#5fb043"/>
      <stop offset="1" stop-color="#2a963f"/>
    </linearGradient>
  </defs>
</svg>

<!-- Outside back -->
<div class="card" style="left:67px;top:96px">
  <svg class="bg" viewBox="0 0 516 288">
    <rect width="516" height="288" fill="url(#blueGrad)"/>
    <path d="M262,0 C250,90 272,200 258,288 L516,288 L516,0Z" fill="url(#greenGrad)"/>
    <path d="M262,0 C250,90 272,200 258,288" fill="none" stroke="#fff" stroke-width="2"/>
    <circle cx="258" cy="118" r="16" fill="#fff"/>
  </svg>
  <div class="t brand" style="left:0;width:516px;text-align:center;top:144px;font-size:22px">Bluebrook Irrigation</div>
  <div class="t web" style="left:0;width:516px;text-align:center;top:226px;font-size:15px;letter-spacing:5px">www.irrigatepros.com</div>
</div>

<!-- Outside front -->
<div class="card" style="left:607px;top:96px">
  <svg class="bg" viewBox="0 0 516 288">
    <rect width="516" height="288" fill="url(#greenGrad)"/>
    <rect width="60" height="288" fill="url(#blueGrad)"/>
    <path d="M40,0 H240 C270,60 282,150 268,205 C258,245 262,270 272,288 H40Z" fill="#fff"/>
    <circle cx="150" cy="70" r="20" fill="var(--brand-blue)"/>
  </svg>
  <div class="t brand on-white" style="left:40px;width:220px;text-align:center;top:102px;font-size:24px;line-height:1.15;white-space:normal">Bluebrook Irrigation</div>
  <div class="t web" style="right:18px;top:250px;font-size:14px;letter-spacing:1px">www.irrigatepros.com</div>
</div>

<!-- Inside: contact -->
<div class="card" style="left:67px;top:437px">
  <svg class="bg" viewBox="0 0 516 288">
    <rect width="516" height="288" fill="url(#greenGrad)"/>
    <rect width="44" height="288" fill="url(#blueGrad)"/>
    <path d="M30,0 H290 C302,40 302,90 294,130 C284,175 296,240 316,288 H30Z" fill="#fff"/>
    <circle cx="82" cy="112" r="17" fill="var(--brand-blue)"/>
  </svg>
  <div class="t brand on-white small" style="left:50px;top:136px">Bluebrook<br>Irrigation</div>
  <div class="t person-name" style="left:126px;top:104px">Doug Harlan</div>
  <div class="t person-title" style="left:126px;top:136px">General Operations Manager</div>
  <div class="t contact" style="left:322px;top:92px">
    <div class="contact-row" style="margin-bottom:14px">
      <svg viewBox="0 0 12 12"><path d="M6 0.5a4 4 0 0 0-4 4c0 3 4 7 4 7s4-4 4-7a4 4 0 0 0-4-4zm0 5.6a1.6 1.6 0 1 1 0-3.2 1.6 1.6 0 0 1 0 3.2z" fill="#1e2a1e"/></svg>
      <div>742 Orchard Lane<br>Irving, TX 75119</div>
    </div>
    <div class="contact-row">
      <svg viewBox="0 0 12 12"><path d="M3 0.8l2 2.6-1.2 1.3c.7 1.5 1.9 2.7 3.4 3.4L8.5 6.9 11.2 9l-1 2.2C5.2 11 1 6.8.8 1.8z" fill="#1e2a1e"/></svg>
      <div>972-555-0148</div>
    </div>
    <div class="contact-row">
      <svg viewBox="0 0 12 12"><rect x="3" y="0.5" width="6" height="11" rx="1.2" fill="#1e2a1e"/><rect x="4" y="2" width="4" height="6" fill="#fff"/></svg>
      <div>972-555-0192</div>
    </div>
    <div class="contact-row">
      <svg viewBox="0 0 12 12"><rect x="3" y="0.5" width="6" height="4" fill="#1e2a1e"/><rect x="0.5" y="4" width="11" height="5" rx="1" fill="#1e2a1e"/><rect x="3" y="7.5" width="6" height="4" fill="#1e2a1e" stroke="#fff" stroke-width=".8"/></svg>
      <div>972-555-0163</div>
    </div>
    <div class="contact-row">
      <svg viewBox="0 0 12 12"><rect x="0.5" y="2" width="11" height="8" fill="#1e2a1e"/><path d="M1 2.5l5 4 5-4" fill="none" stroke="#fff" stroke-width="1"/></svg>
      <div>doug@irrigatepros.com</div>
    </div>
  </div>
</div>

<!-- Inside: services -->
<div class="card" style="left:607px;top:437px">
  <svg class="bg" viewBox="0 0 516 288">
    <rect width="516" height="288" fill="url(#greenGrad)"/>
    <rect width="44" height="288" fill="url(#blueGrad)"/>
    <path d="M30,0 H122 C138,60 138,110 126,150 C114,195 122,245 138,288 H30Z" fill="#fff"/>
    <circle cx="82" cy="112" r="17" fill="var(--brand-blue)"/>
  </svg>
  <div class="t brand on-white small" style="left:50px;top:136px">Bluebrook<br>Irrigation</div>
  <div class="t services-title" style="left:222px;top:20px">Services we perform</div>
  <ul class="t services" style="left:222px;top:46px">
    <li>Lawn Sprinkler Repair</li>
    <li>Lawn Sprinkler Installation</li>
    <li>Sprinkler System Efficiency Evaluation</li>
    <li>French/Area Drains</li>
    <li>Outdoor Lighting</li>
    <li>Tree/Shrub Planting</li>
    <li>Landscaping</li>
    <li>Water Features</li>
    <li>Sod</li>
    <li>Backflow Testing</li>
    <li>Outdoor/Landscape Lighting</li>
    <li>Soil Test/Analysis</li>
  </ul>
</div>
</body>
</html>
```